Real Estate Investing company needs a business card design

We need a business card design for new Real Estate Investment Company called "Maple Ridge Ventures, LLC." We buy homes for cash and close quickly in any situation. Our company provides an easy and fast option for home owners who are in tough situations who need to sell their home fast and don't want realtor fees or other listing hassles. We also renovate and resell our homes which helps provide housing for the community. We would like to see designs that use the colors blue and white to match our company logo or other colors that may match our company logo. The final design should communicate trust and easy process.
Industry/Entity Type
Business
Contact Information for Business Card
Front should have company name and company logo. back of card should have company logo and area to list services.
Look and feel

```html
<!DOCTYPE html>
<html lang="en">
<head>
<meta charset="utf-8">
<title>Maple Ridge Ventures – Business Card</title>
<link href="https://fonts.googleapis.com/css2?family=Source+Sans+3:wght@400;600;700&display=swap" rel="stylesheet">
<style>
  :root {
    --brand-blue: #0f72ba;
    --ink: #1b1b1b;
    --paper: #ffffff;
    --backdrop-top: #c9c9c9;
    --backdrop-bottom: #b3b3b3;
  }
  * { margin: 0; padding: 0; box-sizing: border-box; }
  html, body { width: 1200px; height: 900px; overflow: hidden; }
  body {
    background: linear-gradient(180deg, var(--backdrop-top), var(--backdrop-bottom));
    font-family: "Source Sans 3", sans-serif;
    position: relative;
  }
  .card {
    position: absolute;
    top: 306px;
    height: 271px;
    border-radius: 10px;
    overflow: hidden;
    background: var(--brand-blue);
    box-shadow: 0 1px 3px rgba(0,0,0,0.25);
  }
  .card--front { left: 149px; width: 439px; }
  .card--back { left: 608px; width: 441px; }
  .card__art { position: absolute; inset: 0; width: 100%; height: 100%; }
  .brand-name {
    position: absolute;
    left: 0; right: 0;
    text-align: center;
    font-weight: 700;
    font-size: 25px;
    line-height: 25px;
    letter-spacing: 0.5px;
  }
  .card--front .brand-name { top: 28px; color: var(--paper); }
  .card--back .brand-name { top: 34px; color: var(--brand-blue); }
  .contact {
    position: absolute;
    top: 172px;
    left: 0; right: 0;
    color: var(--paper);
  }
  .contact__person {
    position: absolute;
    right: 228px;
    text-align: right;
  }
  .contact__name { font-size: 15px; font-weight: 600; line-height: 18px; }
  .contact__role { font-size: 12.5px; line-height: 16px; }
  .contact__lines { position: absolute; left: 229px; font-size: 12.5px; line-height: 16px; }
  .contact__line { display: flex; align-items: center; gap: 6px; }
  .contact__line svg { width: 10px; height: 10px; fill: var(--paper); }
  .address {
    position: absolute;
    top: 220px; left: 0; right: 0;
    text-align: center;
    color: var(--paper);
    font-size: 13px;
  }
  .services {
    position: absolute;
    top: 150px; left: 20px; right: 20px;
    text-align: center;
    color: var(--paper);
    font-size: 13px;
    line-height: 16px;
  }
  .services p + p { margin-top: 6px; }
</style>
</head>
<body>

<section class="card card--front">
  <svg class="card__art" viewBox="0 0 439 271" aria-hidden="true">
    <path d="M0,0 H439 V124 L410,102 V112 H80 L0,57 Z" fill="var(--ink)"/>
    <path d="M0,63 L80,118 H410 V140 H80 L0,86 Z" fill="var(--ink)"/>
    <path d="M0,57 L80,112 H410 V102 L439,124 L410,146 V134 H80 L0,80 Z" fill="var(--brand-blue)"/>
  </svg>
  <div class="brand-name">MAPLE RIDGE<br>VENTURES, LLC</div>
  <div class="contact">
    <div class="contact__person">
      <div class="contact__name">Daniel Reyes</div>
      <div class="contact__role">Managing Director</div>
    </div>
    <div class="contact__lines">
      <div class="contact__line">
        <svg viewBox="0 0 10 10"><path d="M2,0.5 L3.6,2.6 L2.7,3.6 Q3.8,5.9 6.4,7.3 L7.4,6.4 L9.5,8 L8.3,9.5 Q4.5,9 1.5,5 Q0.3,3 0.6,1.6 Z"/></svg>
        <span>044-555 010 200</span>
      </div>
      <div class="contact__line">
        <svg viewBox="0 0 10 10"><path d="M0.5,2 H9.5 V8.5 H0.5 Z"/><path d="M1,2.5 L5,5.6 L9,2.5" stroke="#0f72ba" stroke-width="0.9" fill="none"/></svg>
        <span>info@mapleridge.com</span>
      </div>
    </div>
  </div>
  <div class="address">12345, Address Goes Here Country Name, 123456.</div>
</section>

<section class="card card--back">
  <svg class="card__art" viewBox="0 0 441 271" aria-hidden="true">
    <path d="M0,0 H441 V52 L360,106 H32 V100 L0,122 Z" fill="var(--paper)"/>
    <path d="M441,78 L360,132 H32 V141 H362 L441,88 Z" fill="var(--paper)"/>
    <path d="M441,52 L360,106 H32 V100 L0,122 L32,144 V132 H360 L441,78 Z" fill="var(--brand-blue)"/>
  </svg>
  <div class="brand-name">MAPLE RIDGE<br>VENTURES, LLC</div>
  <div class="services">
    <p>We buy homes for cash and close quickly in any situation.</p>
    <p>Our company provides an easy and fast option for home owners<br>who are in tough situations who need to sell their home fast and<br>don't want realtor fees or other listing hassles.</p>
    <p>We also renovate and resell our homes which helps provide housing<br>for the community.</p>
  </div>
</section>

</body>
</html>
```